Business Card - Professional Minimalist - Double sided

We appreciate minimalist logo/web/collateral designs that allow design to tell a story. We want to relay a professional image/approach but throwing in a splash of modern when we’re able so long as it’s not distracting. Think 75% classic corporate, 25% modern. Open to black or white design, not sure which might look the best.

Target Market(s)

Senior executives or related government affairs contacts within the agriculture, energy, and defense industries (i.e., potential clients) but located outside of Washington, DC. Most potential clients based in DC with be familiar with both of us and our shared history.

Industry/Entity Type

Consulting

Contact Information for Business Card

Name: Daniel R. Whitlock
Title: Co-Founder & Partner
Address: 418 Bramblewood Ave. SE | Suite 2716 | Washington, D.C. 20019
Phone: (202) 555-0187
Email: Daniel@HollerbyWhitlock.com

Font styles to use
Serif

Colors

Designer to choose only greyscale colors for use in the design.

Requirements
Must have
• Name: Daniel R. Whitlock
Phone: (202) 555-0187

```html
<!DOCTYPE html>
<html lang="en">
<head>
<meta charset="utf-8">
<title>Hollerby Whitlock Group — Business Card</title>
<link rel="stylesheet" href="https://fonts.googleapis.com/css2?family=Montserrat:wght@400;600&family=Lato:wght@400&family=Source+Sans+3:wght@400&display=swap">
<style>
  :root {
    --page: #ffffff;
    --card-front: #ffffff;
    --ink-dark: #4a4a4a;
    --ink-mid: #6a6a6a;
    --ink-soft: #8a8a8a;
    --back-dark: #000000;
    --back-sheen: #5a5a5a;
    --white: #ffffff;
  }
  html, body {
    margin: 0;
    width: 1200px;
    height: 1200px;
    overflow: hidden;
    background: var(--page);
  }
  .canvas {
    position: relative;
    width: 1200px;
    height: 1200px;
  }
  .card {
    position: absolute;
    left: 166px;
    width: 859px;
    height: 515px;
    box-shadow: 3px 5px 8px rgba(0,0,0,0.35);
  }
  .card--front { top: 84px; background: var(--card-front); }
  .card--back {
    top: 636px;
    background:
      radial-gradient(ellipse 90% 110% at 15% 10%, var(--back-sheen) 0%, #2a2a2a 45%, var(--back-dark) 85%),
      var(--back-dark);
  }

  .brand {
    position: absolute;
    left: 56px;
    top: 58px;
    display: flex;
    align-items: center;
  }
  .brand__square {
    width: 66px;
    height: 66px;
    background: var(--ink-mid);
    margin-right: 14px;
  }
  .brand__name {
    font-family: "Montserrat", sans-serif;
    font-weight: 600;
    font-size: 26px;
    letter-spacing: 1px;
    color: var(--ink-dark);
    line-height: 1;
    white-space: nowrap;
  }

  .person {
    position: absolute;
    left: 56px;
    top: 290px;
  }
  .person__name {
    font-family: "Montserrat", sans-serif;
    font-weight: 600;
    font-size: 27px;
    letter-spacing: 0.5px;
    color: var(--ink-dark);
    line-height: 1;
  }
  .person__title {
    font-family: "Montserrat", sans-serif;
    font-weight: 400;
    font-size: 20px;
    letter-spacing: 0.5px;
    color: var(--ink-soft);
    margin-top: 6px;
    line-height: 1;
  }

  .contact {
    position: absolute;
    left: 56px;
    top: 384px;
    font-family: "Source Sans 3", sans-serif;
    color: var(--ink-soft);
    font-size: 19px;
  }
  .contact__row {
    display: flex;
    align-items: center;
    height: 26.5px;
    white-space: nowrap;
  }
  .contact__row--phone { font-family: "Lato", sans-serif; font-size: 20px; }
  .contact__icon {
    width: 15px;
    height: 15px;
    margin-right: 12px;
    fill: var(--ink-mid);
  }
  .contact__row--email { letter-spacing: 1.2px; }

  .divider {
    position: absolute;
    left: 402px;
    top: 390px;
    width: 1.5px;
    height: 70px;
    background: var(--ink-mid);
  }
  .address {
    position: absolute;
    left: 420px;
    top: 384px;
    font-family: "Lato", sans-serif;
    font-style: normal;
    font-size: 19.5px;
    line-height: 26.5px;
    color: var(--ink-soft);
    white-space: nowrap;
  }

  .pattern-field {
    position: absolute;
    inset: 0;
  }
  .back-mark {
    position: absolute;
    right: 66px;
    bottom: 66px;
    display: flex;
    align-items: center;
    font-family: "Montserrat", sans-serif;
    font-weight: 600;
    font-size: 14px;
    letter-spacing: 0.5px;
    color: var(--white);
    white-space: nowrap;
  }
  .back-mark__square {
    width: 36px;
    height: 36px;
    background: var(--white);
    margin-right: 10px;
  }
</style>
</head>
<body>
<main class="canvas">

  <section class="card card--front" aria-label="Card front">
    <div class="brand">
      <span class="brand__square"></span>
      <span class="brand__name">HOLLERBY WHITLOCK GROUP</span>
    </div>

    <div class="person">
      <div class="person__name">DANIEL R. WHITLOCK</div>
      <div class="person__title">Co-Founder &amp; Partner</div>
    </div>

    <div class="contact">
      <div class="contact__row contact__row--phone">
        <svg class="contact__icon" viewBox="0 0 24 24" aria-hidden="true"><path d="M6.6 10.8a15.1 15.1 0 0 0 6.6 6.6l2.2-2.2a1 1 0 0 1 1-.25 11.4 11.4 0 0 0 3.6.57 1 1 0 0 1 1 1V20a1 1 0 0 1-1 1A17 17 0 0 1 3 4a1 1 0 0 1 1-1h3.5a1 1 0 0 1 1 1c0 1.25.2 2.45.57 3.57a1 1 0 0 1-.25 1z"/></svg>
        (202) 555-0187
      </div>
      <div class="contact__row contact__row--email">
        <svg class="contact__icon" viewBox="0 0 24 24" aria-hidden="true"><path d="M2 5h20v14H2z M2 5l10 8 10-8" stroke="#fff" stroke-width="1.5"/></svg>
        Daniel@HollerbyWhitlock.com
      </div>
      <div class="contact__row">
        <svg class="contact__icon" viewBox="0 0 24 24" aria-hidden="true"><circle cx="12" cy="12" r="10"/><path d="M7 8c2 0 3 1 3 3s2 2 2 4-1 3-1 5M15 4c0 2 2 3 4 3" stroke="#fff" stroke-width="1.5" fill="none"/></svg>
        www.DanielHollerbyWhitlock.com
      </div>
    </div>

    <div class="divider"></div>

    <address class="address">
      418 Bramblewood Ave.<br>
      SE | Suite 2716 | Washington,<br>
      D.C. 20019
    </address>
  </section>

  <section class="card card--back" aria-label="Card back">
    <div class="pattern-field" role="img" aria-label="Repeating grey brand pattern with a silver sheen on black"></div>
    <div class="back-mark"><span class="back-mark__square"></span>HOLLERBY WHITLOCK</div>
  </section>

</main>
</body>
</html>
```